K8 FIRST WEBSITE FOR CONCRETE DESIGN START-UP

We would like a 3-4 page website. Very basic. About Us, Pricing, Testimonials, Pictures and somewhere they can contact us. We are a concrete design/epoxy company. Want clean/modern and something that is user friendly that we can keep building on. Important we can update the website and that it shows good examples of our work.
Target Market(s)
Home owners or business owners who want unique solutions to concrete flooring in garages, patios, basements, showrooms or anywhere concrete is or can be.
Industry/Entity Type
Concrete
Coding
Coded - Design and coding required
Number of Pages Required
4 page
Look and feel

```html
<!DOCTYPE html>
<html lang="en">
<head>
<meta charset="utf-8">
<title>K8 Concrete</title>
<link href="https://fonts.googleapis.com/css2?family=Poppins:wght@300;400;500;600;700&family=Libre+Baskerville:ital@1&display=swap" rel="stylesheet">
<style>
:root{
  --orange:#f26a21;
  --orange-dark:#e55a12;
  --ink:#1f1f1f;
  --text:#555;
  --muted:#8a8a8a;
  --light:#f3f3f3;
  --line:#e3e3e3;
  --charcoal:#2d2d2d;
  --white:#fff;
}
*{box-sizing:border-box;margin:0;padding:0}
html,body{width:1200px;height:3704px;overflow:hidden}
body{position:relative;background:var(--white);font-family:"Poppins",sans-serif;color:var(--ink)}
.abs{position:absolute}
svg{display:block}
.brand{display:flex;align-items:center;gap:8px;font-weight:700;color:var(--ink);letter-spacing:1px}
.brand-square{width:14px;height:14px;background:var(--orange)}

/* header */
.site-header{position:absolute;left:0;top:0;width:1200px;height:89px;background:var(--white);border-bottom:1px solid var(--line)}
.site-header .brand{position:absolute;left:234px;top:26px;font-size:24px}
.top-contact{position:absolute;top:14px;display:flex;gap:8px;align-items:flex-start}
.top-contact small{display:block;font-size:7px;color:var(--muted);letter-spacing:.3px}
.top-contact span{display:block;font-size:11px;color:var(--orange);margin-top:2px}
.main-nav{position:absolute;top:57px;left:470px;display:flex;font-size:10px;font-weight:500;letter-spacing:.3px}
.main-nav a{color:var(--ink);text-decoration:none;padding:0 17px;border-left:1px solid #ddd;line-height:12px}
.main-nav a:first-child{border-left:0;color:var(--orange);position:relative}
.main-nav a:first-child::after{content:"";position:absolute;left:14px;right:14px;top:30px;height:3px;background:var(--orange)}

/* hero */
.hero{position:absolute;left:0;top:89px;width:1200px;height:431px}
.hero > svg{position:absolute;left:0;top:0}
.hero-title{position:absolute;left:0;width:1200px;top:202px;text-align:center;color:var(--white);font-size:25px;font-weight:500;line-height:32px;letter-spacing:1px;text-shadow:0 1px 3px rgba(0,0,0,.4)}
.play{position:absolute;left:577px;top:136px;width:45px;height:45px;border-radius:50%;background:var(--white);display:flex;align-items:center;justify-content:center}
.slide-arrow{position:absolute;top:173px;width:32px;height:35px;background:rgba(255,255,255,.75);display:flex;align-items:center;justify-content:center;font-size:16px;color:#333}
.btn{display:inline-flex;align-items:center;justify-content:center;font-weight:600;font-size:11px;letter-spacing:.5px;color:var(--white)}
.hero .btn{position:absolute;top:287px;height:34px;border-radius:17px;box-shadow:0 3px 6px rgba(0,0,0,.3)}
.btn-grey{background:linear-gradient(#9a9a9a,#6c6c6c)}
.btn-orange{background:var(--orange)}

/* welcome */
.welcome .brand{position:absolute;left:234px;top:594px;font-size:18px}
.eyebrow{position:absolute;left:234px;top:648px;font-size:12px;font-weight:600;z-index:2}
.welcome-sub{position:absolute;left:234px;top:673px;width:280px;font-size:13px;font-weight:600;color:var(--orange);line-height:19px;z-index:2}
.welcome-copy{position:absolute;left:234px;top:721px;width:270px;font-size:9.3px;line-height:16.2px;color:var(--text);text-align:justify;z-index:2}
.btn-square{position:absolute;height:34px;background:var(--orange);font-size:11px}
.btn-square::after{content:"";position:absolute;right:8px;top:0;width:3px;height:34px;background:var(--white)}
.welcome-photo{position:absolute;left:540px;top:612px;width:580px;height:296px;border-radius:4px;background:linear-gradient(120deg,#8b857c,#c5c0b6 45%,#6f6a63)}

.stats{position:absolute;top:963px;left:0;width:1200px;height:72px}
.stat{position:absolute;top:0;height:72px;background:var(--white);border-radius:36px;box-shadow:0 2px 10px rgba(0,0,0,.12);display:flex;align-items:center;gap:12px;padding:0 18px}
.stat b{font-size:32px;font-weight:600;color:var(--orange)}
.stat span{font-size:11px;font-weight:600;line-height:15px}

/* specialties */
.specialties{position:absolute;left:0;top:1104px;width:1200px;height:630px}
.specialties svg{position:absolute;left:0;top:0}
.section-title{position:absolute;left:0;width:1200px;text-align:center;font-size:25px;font-weight:600;letter-spacing:.5px}
.section-rule{position:absolute;left:574px;width:52px;height:2px;background:var(--orange)}
.section-lead{position:absolute;left:0;width:1200px;top:1238px;text-align:center;font-size:10.5px;line-height:19px;color:var(--text)}
.service{position:absolute;top:1318px;width:168px;height:266px;background:var(--white);border-top:2px solid var(--orange);text-align:center}
.service .ph{height:114px}
.service h3{font-size:12px;font-weight:600;margin-top:28px}
.service p{font-size:9px;line-height:15px;color:var(--text);margin:8px 10px 0}
.plus{position:absolute;left:69px;bottom:-16px;width:30px;height:30px;border-radius:50%;background:var(--orange);color:var(--white);font-size:16px;display:flex;align-items:center;justify-content:center}
.dots{position:absolute;display:flex;gap:6px;align-items:center}
.dot{width:8px;height:8px;border-radius:50%;background:#ccc}
.dot.on{width:11px;height:11px;background:none;border:2px solid var(--orange)}

/* projects */
.filters{position:absolute;left:234px;top:1897px;width:106px;height:306px;border-right:1px solid var(--line)}
.filters li{list-style:none;height:37.5px;line-height:37.5px;text-align:right;padding-right:12px;font-size:10px;font-weight:500;border-bottom:1px solid var(--line);white-space:nowrap}
.filters li.on{color:var(--orange);border-left:3px solid var(--orange);font-size:9px}
.tile{position:absolute;overflow:hidden}
.tile span{position:absolute;left:0;right:0;bottom:0;height:28px;line-height:28px;text-align:center;color:var(--white);font-size:10px;font-weight:500;background:rgba(0,0,0,.55)}

/* testimonials */
.testimonials{position:absolute;left:0;top:2275px;width:1200px;height:340px;background:var(--charcoal)}
.avatar{position:absolute;left:567px;top:2414px;width:66px;height:66px;border-radius:50%;background:linear-gradient(#d9b59a,#b98a6a);border:3px solid var(--white)}
.quote{position:absolute;left:0;width:1200px;top:2500px;text-align:center;font-family:"Libre Baskerville",serif;font-style:italic;font-size:12.5px;line-height:16px;color:#ddd}
.quote-mark{position:absolute;left:292px;top:2480px;font-family:"Libre Baskerville",serif;font-size:48px;color:#666}

/* quote form */
.quote-section{position:absolute;left:0;top:2615px;width:1200px;height:748px;background:var(--orange)}
.form-card{position:absolute;left:445px;top:2821px;width:307px;height:477px;background:var(--white)}
.form-card label{position:absolute;left:28px;font-size:8.5px;color:#444;letter-spacing:.2px}
.field{position:absolute;left:28px;width:251px;height:29px;border:1px solid #ccc;font-size:8.5px;color:#aaa;padding:9px 12px}
.send{position:absolute;left:81px;top:414px;width:144px;height:34px;background:var(--ink);font-size:11px}
.send::after{content:"";position:absolute;right:16px;top:0;width:3px;height:34px;background:var(--white)}

/* footer */
.footer-links{position:absolute;left:233px;top:3420px;list-style:none;font-size:10.5px}
.footer-links li{height:26.3px}
.footer-divider{position:absolute;top:3420px;width:1px;height:148px;background:var(--line)}
.social{position:absolute;top:3528px;width:48px;height:48px;border-radius:50%;border:1px solid #ccc;display:flex;align-items:center;justify-content:center}
.footer-info{position:absolute;left:851px;top:3420px;font-size:10.5px;line-height:16px}
.footer-info small{display:block;color:var(--muted)}
.copyright{position:absolute;left:0;width:1200px;top:3652px;text-align:center;font-size:10px;color:#555}
</style>
</head>
<body>

<header class="site-header">
  <div class="brand"><i class="brand-square"></i>K8 CONCRETE</div>
  <div class="top-contact" style="left:696px">
    <svg width="20" height="18" viewBox="0 0 20 18"><path d="M1 7 L10 1 L19 7 V17 H1 Z M1 7 L10 12 L19 7" fill="none" stroke="#888" stroke-width="1.2"/></svg>
    <div><small>WANT AN APPROXIMATE PRICE?</small><span>GET A FREE QUOTE »</span></div>
  </div>
  <div class="top-contact" style="left:860px">
    <svg width="20" height="18" viewBox="0 0 20 18"><path d="M4 2 L8 6 L6 8 Q9 12 12 13 L14 11 L18 15 L15 17 Q5 15 2 5 Z" fill="none" stroke="#888" stroke-width="1.2"/></svg>
    <div><small>CALL US NOW:</small><span>555-014-2290</span></div>
  </div>
  <nav class="main-nav">
    <a>HOME</a><a>ABOUT US</a><a>PRICING</a><a>TESTIMONIALS</a><a>GALLERY</a><a>CONTACT US</a>
  </nav>
</header>

<section class="hero">
  <svg width="1200" height="431" viewBox="0 0 1200 431">
    <defs><linearGradient id="garage" x1="0" y1="0" x2="0" y2="1"><stop offset="0" stop-color="#b9b8b4"/><stop offset=".45" stop-color="#9d9992"/><stop offset="1" stop-color="#8a847c"/></linearGradient></defs>
    <polygon role="img" aria-label="Garage with speckled epoxy floor coating" points="0,0 1200,0 1200,364 600,412 0,364" fill="url(#garage)"/>
    <polygon points="0,364 600,412 1200,364 1200,370 600,431 0,370" fill="var(--orange)"/>
  </svg>
  <div class="slide-arrow" style="left:62px">‹</div>
  <div class="slide-arrow" style="left:1099px">›</div>
  <div class="play"><svg width="14" height="16" viewBox="0 0 14 16"><polygon points="2,1 13,8 2,15" fill="#f26a21"/></svg></div>
  <h1 class="hero-title">K8 EPOXY FLOOR AND DECORATIVE<br>CONCRETE COATING EXPERTS</h1>
  <span class="btn btn-grey" style="left:470px;width:122px">LEARN MORE</span>
  <span class="btn btn-orange" style="left:605px;width:125px">GET QUOTE</span>
</section>

<section class="welcome">
  <div class="welcome-photo" role="img" aria-label="Worker grinding a concrete floor"></div>
  <div class="brand"><i class="brand-square"></i>K8</div>
  <p class="eyebrow">WELCOME TO K8 CONCRETE</p>
  <p class="welcome-sub">COATING, EPOXY, FLAT WORK,<br>POLISHED CONRETE, CUTTING &amp; CORING</p>
  <p class="welcome-copy">Lorem ipsum dolor sit amet, consectetur adipiscing elit. Mauris in rhoncus quam. Nulla facilisi. Nunc vestibulum convallis rutrum. Vivamus eros nisi, aliquam vel enim in, consectetur ultricies felis. Sed a purus non neque pulvinar molestie eu ac odio. Morbi condimentum porta tellus, sit amet tempus orci ornare a. Vestibulum sit amet cursus lectus. Fusce molestie, tellus id gravida mollis, quam felis rhoncus nulla, nec facilisis felis quam sollicitudin mi.</p>
  <span class="btn btn-square" style="left:234px;top:874px;width:144px;padding-right:14px">LEARN MORE</span>
</section>

<div class="stats">
  <div class="stat" style="left:201px;width:196px"><b>450</b><span>CONCRETE<br>WORK DONE</span></div>
  <div class="stat" style="left:411px;width:168px"><b>10</b><span style="text-align:right">YEARS<br>EXPERIENCED<br>COMPANY</span></div>
  <div class="stat" style="left:586px;width:193px;justify-content:space-between"><span>UPCOMMING<br>PROJECTS</span><b>45</b></div>
  <div class="stat" style="left:793px;width:196px"><b>50</b><span>RUNNING<br>PROJECTS</span></div>
</div>

<section class="specialties">
  <svg width="1200" height="630" viewBox="0 0 1200 630">
    <polygon points="0,0 1200,0 1200,560 600,612 0,560" fill="var(--light)"/>
    <polygon points="0,560 600,612 1200,560 1200,564 600,630 0,564" fill="var(--orange)"/>
  </svg>
</section>
<h2 class="section-title" style="top:1160px">WE SPECIALIZING IN</h2>
<i class="section-rule" style="top:1211px"></i>
<p class="section-lead">Lorem ipsum dolor sit amet, consectetur adipiscing elit. Mauris in rhoncus quam. Nulla facilisi.<br>Nunc vestibulum convallis rutrum. Vivamus eros nisi, aliquam vel enim.</p>

<article class="service" style="left:234px"><div class="ph" role="img" aria-label="Coated concrete floor" style="background:linear-gradient(135deg,#9c9a96,#d7d4cf)"></div><h3>COATING</h3><p>Lorem ipsum dolor sit amet, consectetur adipiscing elit. Mauris in rhoncus quam. Nulla facilisi. Nunc vestibulum.</p><span class="plus">+</span></article>
<article class="service" style="left:421px"><div class="ph" role="img" aria-label="Close-up of epoxy aggregate floor" style="background:linear-gradient(135deg,#8d8479,#c2b7a8)"></div><h3>EPOXY</h3><p>Lorem ipsum dolor sit amet, consectetur adipiscing elit. Mauris in rhoncus quam. Nulla facilisi. Nunc vestibulum.</p><span class="plus">+</span></article>
<article class="service" style="left:609px"><div class="ph" role="img" aria-label="Floor grinding machine" style="background:linear-gradient(135deg,#5b5752,#a8a39a)"></div><h3>FLAT WORK</h3><p>Lorem ipsum dolor sit amet, consectetur adipiscing elit. Mauris in rhoncus quam. Nulla facilisi. Nunc vestibulum.</p><span class="plus">+</span></article>
<article class="service" style="left:796px"><div class="ph" role="img" aria-label="Polished concrete in an empty room" style="background:linear-gradient(#9d9d9d,#5e3a30)"></div><h3>POLISHED CONRETE</h3><p>Lorem ipsum dolor sit amet, consectetur adipiscing elit. Mauris in rhoncus quam. Nulla facilisi. Nunc vestibulum.</p><span class="plus">+</span></article>
<div class="dots" style="left:586px;top:1649px"><i class="dot on"></i><i class="dot"></i></div>

<h2 class="section-title" style="top:1798px">RECENT PROJECTS</h2>
<i class="section-rule" style="top:1851px"></i>
<ul class="filters">
  <li class="on">ALL</li><li>Coating</li><li>Epoxy</li><li>Flat Work</li><li>Polished Concrete</li><li>Cutting</li><li>Coring</li>
</ul>
<div class="tile" role="img" aria-label="Marbled polished concrete" style="left:359px;top:1897px;width:194px;height:146px;background:linear-gradient(135deg,#3d2e28,#b6a79b 50%,#4a3a33)"><span>Polished Concrete</span></div>
<div class="tile" role="img" aria-label="Grinding machine on floor" style="left:565px;top:1897px;width:194px;height:306px;background:linear-gradient(#c9b39d,#6d665e)"><span>Flat Work</span></div>
<div class="tile" role="img" aria-label="Polished concrete room" style="left:772px;top:1897px;width:194px;height:146px;background:linear-gradient(#9a9a9a,#5c3b33)"><span>Polished Concrete</span></div>
<div class="tile" role="img" aria-label="Epoxy floor with equipment" style="left:359px;top:2056px;width:194px;height:147px;background:linear-gradient(135deg,#6f6d69,#b8b5b0)"><span>Epoxy</span></div>
<div class="tile" role="img" aria-label="Worker cutting concrete outdoors" style="left:772px;top:2056px;width:194px;height:147px;background:linear-gradient(#7ea3d0,#c9b9a4)"><span>Cutting</span></div>

<section class="testimonials"></section>
<h2 class="section-title" style="top:2334px;color:var(--white)">HAPPY CUSTOMERS</h2>
<span class="abs" style="left:546px;top:2438px;color:#ccc;font-size:14px">‹</span>
<span class="abs" style="left:645px;top:2438px;color:#ccc;font-size:14px">›</span>
<div class="avatar" role="img" aria-label="Customer portrait"></div>
<span class="quote-mark">“</span>
<p class="quote">Lorem ipsum dolor sit amet, consectetur adipiscing elit. Cras vitae sagittis lectus. Aliquam erat volutpat.<br>Etiam eu suscipit lorem. Ut eget massa venenatis, pellentesque nibh et, fermentum odio. Sed in cursus<br>urna. Quisque eu mi tortor. Pellentesque cursus turpis tellus, semper vehicula justo ornare vel.</p>
<p class="abs" style="left:0;width:1200px;top:2574px;text-align:center;color:var(--white);font-size:11px">DANA REYES</p>
<p class="abs" style="left:0;width:1200px;top:2591px;text-align:center;color:#bbb;font-size:8.5px">Customer</p>

<section class="quote-section"></section>
<div class="dots" style="left:583px;top:2623px"><i class="dot" style="background:var(--white)"></i><i class="dot" style="background:#f7a37a"></i><i class="dot" style="background:#f7a37a"></i></div>
<h2 class="section-title" style="top:2731px;color:var(--white)">GET A FREE QUOTE</h2>
<i class="section-rule" style="top:2783px;background:var(--charcoal)"></i>
<form class="form-card">
  <label style="top:26px">NAME:</label><div class="field" style="top:40px">First &amp; Last</div>
  <label style="top:82px">TELEPHONE:</label><div class="field" style="top:96px">+44 XXX XXX</div>
  <label style="top:139px">DESCRIPTION OF REQUIRED WORK:</label><div class="field" style="top:153px">Epoxy<svg class="abs" style="right:12px;top:12px" width="8" height="5" viewBox="0 0 8 5"><polygon points="0,0 8,0 4,5" fill="#333"/></svg></div>
  <label style="top:197px">WHEN DO YOU NEED THIS WORK TO BE COMPLETED?</label><div class="field" style="top:211px">Next Week..?</div>
  <label style="top:253px">ADDRESS:</label><div class="field" style="top:268px">City, Floor...</div>
  <label style="top:313px">MESSAGE:</label><div class="field" style="top:328px;height:62px">Additional Information</div>
  <span class="btn send" style="position:absolute;padding-right:20px">SEND NOW</span>
</form>

<ul class="footer-links">
  <li>Home</li><li>About Us</li><li>Pricing</li><li>Testimonials</li><li>Gallery</li><li>Contact Us</li>
</ul>
<i class="footer-divider" style="left:428px"></i>
<i class="footer-divider" style="left:769px"></i>
<div class="brand abs" style="left:528px;top:3454px;font-size:26px"><i class="brand-square"></i>K8 CONCRETE</div>
<div class="social" style="left:522px"><svg width="14" height="14" viewBox="0 0 14 14"><circle cx="7" cy="7" r="5.5" fill="none" stroke="#777" stroke-width="1.3"/></svg></div>
<div class="social" style="left:577px"><svg width="14" height="14" viewBox="0 0 14 14"><rect x="1.5" y="1.5" width="11" height="11" fill="none" stroke="#777" stroke-width="1.3"/></svg></div>
<div class="social" style="left:631px"><svg width="14" height="14" viewBox="0 0 14 14"><circle cx="7" cy="7" r="5.5" fill="#777"/></svg></div>
<div class="footer-info">
  <small>Address:</small>21, Lorem Ipsum<br>Dolor Sit, CY 10450
  <small style="margin-top:14px">Phone:</small><span style="font-size:14px;font-weight:500">555-014-2290</span>
  <small style="margin-top:14px">Email:</small><span style="color:var(--orange)">info@k8concrete.com</span>
</div>
<i class="abs" style="left:234px;top:3617px;width:732px;height:1px;background:var(--line)"></i>
<p class="copyright">© 2019 K8 CONCRETE. All rights reserved. &nbsp;|&nbsp; Privacy Policy</p>

</body>
</html>
```